Marrowgate Auctions Business Cards Design Needed

I need a business card design that is modern looking - double sided (maybe just my logo on the back, but open to suggestions) - the overall design is up to you. I want it to be easy to read - not over the top flashy. I already have a company logo which I uploaded so that needs to be used. The colors of my logo are the colors I want on the card... so blue and gray (do need to match the logo colors).

Requirements
Must have
• Would like the card to be sleek, modern and easy to ready

```html
<!DOCTYPE html>
<html lang="en">
<head>
<meta charset="utf-8">
<title>Marrowgate Auctions — Business Cards</title>
<link href="https://fonts.googleapis.com/css2?family=Open+Sans:wght@400;600;700&display=swap" rel="stylesheet">
<style>
  :root {
    --backdrop: #2b2b2b;
    --card-light: #f2f2f2;
    --brand-blue: #2a78b8;
    --text-gray: #454545;
    --white: #ffffff;
  }
  * { margin: 0; padding: 0; box-sizing: border-box; }
  html, body { width: 1200px; height: 1050px; overflow: hidden; }
  body {
    background: var(--backdrop);
    font-family: "Open Sans", sans-serif;
    position: relative;
  }
  .card {
    position: absolute;
    left: 180px;
    width: 840px;
    height: 480px;
    box-shadow: 0 6px 18px rgba(0,0,0,0.45);
  }
  .card--front { top: 20px; background: var(--card-light); }
  .card--back { top: 550px; background: var(--brand-blue); }

  .person { position: absolute; left: 32px; top: 92px; }
  .person__name {
    color: var(--brand-blue);
    font-weight: 600;
    font-size: 40px;
    line-height: 1;
  }
  .person__title {
    color: var(--text-gray);
    font-weight: 600;
    font-size: 23px;
    margin-top: 4px;
  }

  .contact { position: absolute; left: 32px; top: 365px; list-style: none; }
  .contact__item {
    display: flex;
    align-items: center;
    gap: 9px;
    color: var(--text-gray);
    font-size: 23px;
    line-height: 30px;
  }
  .contact__icon { width: 17px; height: 17px; fill: none; stroke: var(--brand-blue); stroke-width: 1.8; }

  .brand {
    position: absolute;
    right: 32px;
    top: 270px;
    display: flex;
    align-items: center;
    gap: 12px;
  }
  .brand__square { width: 22px; height: 22px; background: var(--brand-blue); }
  .brand__name {
    color: var(--brand-blue);
    font-weight: 700;
    font-size: 36px;
  }

  .website {
    position: absolute;
    right: 32px;
    top: 382px;
    color: var(--text-gray);
    font-size: 23px;
  }
  .website__domain { color: var(--brand-blue); font-weight: 600; }

  .back-brand {
    position: absolute;
    left: 0; right: 0;
    top: 170px;
    display: flex;
    flex-direction: column;
    align-items: center;
    gap: 22px;
  }
  .back-brand__square { width: 54px; height: 54px; background: var(--white); }
  .back-brand__name {
    color: var(--white);
    font-weight: 700;
    font-size: 44px;
    line-height: 1;
  }
  .tagline {
    position: absolute;
    left: 0; right: 0;
    top: 398px;
    text-align: center;
    color: var(--white);
    font-size: 23px;
  }
</style>
</head>
<body>
  <section class="card card--front">
    <div class="person">
      <h1 class="person__name">Owen Harlow</h1>
      <p class="person__title">Owner/President - Auctioneer</p>
    </div>

    <ul class="contact">
      <li class="contact__item">
        <svg class="contact__icon" viewBox="0 0 24 24" aria-hidden="true">
          <path d="M5 3h4l2 5-3 2a12 12 0 0 0 6 6l2-3 5 2v4a2 2 0 0 1-2 2A18 18 0 0 1 3 5a2 2 0 0 1 2-2z"/>
        </svg>
        <span>555-214-7380</span>
      </li>
      <li class="contact__item">
        <svg class="contact__icon" viewBox="0 0 24 24" aria-hidden="true">
          <rect x="2" y="5" width="20" height="14"/>
          <path d="M2 5l10 8 10-8"/>
        </svg>
        <span>owen@marrowgateauctions.com</span>
      </li>
    </ul>

    <div class="brand">
      <span class="brand__square"></span>
      <span class="brand__name">Marrowgate</span>
    </div>

    <p class="website">www.<span class="website__domain">marrowgatebids</span>.com</p>
  </section>

  <section class="card card--back">
    <div class="back-brand">
      <span class="back-brand__square"></span>
      <span class="back-brand__name">Marrowgate Auctions</span>
    </div>
    <p class="tagline">Improving Charity Auctions Nationwide</p>
  </section>
</body>
</html>
```